Make a medical leaflet for my patients undergoing ankle blocks

I have a very boring text only leaflet I would like to turn into a professional appealing medical leaflet to give to my patients. I would like to get this onto two pages of a4 if possible and its intended for electronic distribution mainly.
This will be for patients so it must be professional.
It must also contain a copyright logo on it and my name near the start (Dr Tobias Wendell) so my colleagues can't use it easily.
Target Market(s)
Patients undergoing surgery
Industry/Entity Type
Medical
Font styles to use
Other font styles liked:
- no idea, you tell me
Requirements
Must have
- the information contained on the attachment
- look professional
- a copyright on it
Nice to have
- the ashbury clinic logo
Should not have
- Any spelling, grammatical or linguistic errors
- Any font less than size 12

```html
<!DOCTYPE html>
<html lang="en">
<head>
<meta charset="utf-8">
<title>Ankle Block – Patient Information</title>
<link href="https://fonts.googleapis.com/css2?family=Arimo:wght@400;700&display=swap" rel="stylesheet">
<style>
:root{
  --brand:#1f50e3;
  --ink:#3d3d3d;
  --paper:#ffffff;
  --rule:#9aa4b8;
  --footer-grey:#6d7276;
  --hospital:#2a3aa0;
}
*{margin:0;padding:0;box-sizing:border-box}
html,body{width:1200px;height:831px;overflow:hidden;background:var(--paper)}
body{font-family:"Arimo",Helvetica,Arial,sans-serif;color:var(--ink);font-weight:400;position:relative}
.page{position:absolute;top:0;height:831px;width:600px}
.page--one{left:0}
.page--two{left:612px}

.clinic-name{position:absolute;top:48px;left:0;width:588px;display:flex;align-items:center;justify-content:center;gap:8px;
  color:var(--brand);font-size:14px;font-weight:400;line-height:16px}
.clinic-name i{display:block;width:12px;height:12px;background:var(--brand)}

.marker{position:absolute;left:0;width:14px;height:21px;background:var(--brand)}
.marker--light{background:var(--paper)}
.heading{position:absolute;left:23px;font-size:12.4px;font-weight:400;color:var(--brand);letter-spacing:.2px;text-transform:uppercase;line-height:15px}
.band{position:absolute;left:0;background:var(--brand);color:#fff}
.band .heading{color:#fff}

.copy{position:absolute;font-size:9.2px;line-height:11.4px}
.copy p+p{margin-top:11.4px}
.sub{font-weight:700;color:var(--brand);font-size:9.2px;line-height:11.4px}
ul.list{list-style:none}
ul.list li{position:relative;padding-left:11px}
ul.list li::before{content:"";position:absolute;left:2px;top:4px;width:3.6px;height:3.6px;border-radius:50%;background:currentColor}

.benefits{position:absolute;left:23px;top:283px;font-size:10px;line-height:15.6px;list-style:none;color:#fff}
.benefits li{display:flex}
.benefits span{width:35px}

.notice{position:absolute;left:294px;top:696px;width:294px;height:65px;background:var(--brand);color:#fff;padding:11px 6px;font-size:9.2px;line-height:13.6px;text-transform:uppercase}
.notice b{font-weight:700;display:block;margin-bottom:6px}

.hospital{position:absolute;top:777px;width:160px;text-align:center;color:var(--hospital);font-weight:400;font-size:11px;line-height:14px}
.hospital small{display:block;font-size:7px;line-height:10px}
.rule{position:absolute;top:808px;height:1px;background:var(--rule)}
.copyright{position:absolute;top:809px;left:14px;height:22px;width:104px;background:var(--footer-grey);color:#fff;font-size:8px;line-height:22px;padding-left:9px}

.alt-list{position:absolute;left:23px;top:366px;font-size:10px;line-height:20px;list-style:none;color:#fff}
.alt-list li{position:relative;padding-left:14px}
.alt-list li::before{content:"";position:absolute;left:2px;top:8px;width:4px;height:4px;border-radius:50%;background:#fff}
</style>
</head>
<body>

<section class="page page--one">
  <div class="clinic-name"><i></i>The Ashbury Clinic</div>

  <div class="marker" style="top:113px"></div>
  <h1 class="heading" style="top:117px">Ankle Block</h1>
  <div class="copy" style="left:23px;top:136px;width:270px">
    <p>You are scheduled to have surgery on your foot. It is my normal practice to offer and perform (with your consent) an ankle block. This is an optional injection of numbing liquid to the nerves which supply your foot. The ankle block can be performed when you are awake, sedated or under general anaesthesia.</p>
    <p>The ankle block can be combined with a general anaesthetic and with sedation. It can also be used to allow surgery to be performed with you wide awake in certain cases.</p>
  </div>
  <div class="copy" style="left:299px;top:136px;width:270px">
    <p>Having or not having an ankle block does not change the preoperative fasting guidelines you have been given.</p>
    <p>There is a fee for performing an ankle block. Please consult my initial introductory email and terms of business for details</p>
  </div>

  <div class="band" style="top:246px;width:588px;height:124px">
    <div class="marker marker--light" style="top:12px"></div>
    <h2 class="heading" style="top:17px">What are the benefits</h2>
  </div>
  <ol class="benefits">
    <li><span>1 -</span>Excellent pain relief - usually 10-14 hours (and rarely 24-48 hours)</li>
    <li><span>2 -</span>Avoiding traditional painkillers which resulting in less post operative nausea and vomiting</li>
    <li><span>3 -</span>The option to avoid a general anaesthetic (if you wish)</li>
    <li><span>4 -</span>A faster recovery from the general anaesthetic</li>
    <li><span>5 -</span>Certain surgery requires an overnight stay in hospital without an ankle block</li>
  </ol>

  <div class="marker" style="top:383px"></div>
  <h2 class="heading" style="top:388px">What are the risks</h2>
  <div class="copy" style="left:23px;top:409px;width:540px"><p>As with all injections, there is the risk of bruising, bleeding and infection.</p></div>

  <div class="copy" style="left:23px;top:428px;width:272px">
    <div class="sub">1. NERVE DAMAGE</div>
    <ul class="list">
      <li>Occurs 1 in 5000 nerve blocks.</li>
      <li>Creates an area of numbness or weakness/paralysis in some/ all the foot.</li>
      <li>Majority of nerve injuries will heal themselves within a year.</li>
      <li>There is no treatment to fix it.</li>
      <li>If the block has not worn off after 72 hours please let me know.</li>
    </ul>
  </div>
  <div class="copy" style="left:23px;top:516px;width:272px">
    <div class="sub">2. FAILURE</div>
    <ul class="list">
      <li>The success rate with ankle blocks is 98-99%.</li>
      <li>Some blocks will fail, partially or totally.</li>
      <li>If total failure, I will discuss repeating the block with your consent.</li>
    </ul>
  </div>
  <div class="copy" style="left:299px;top:428px;width:272px">
    <div class="sub">3.&nbsp; PAIN DURING OPERATION</div>
    <ul class="list">
      <li>If you choose to have wide awake surgery or surgery under sedation.</li>
      <li>The surgery will stop and I will discuss three options with you.<br>- more numbing liquid to be injected by the surgeon.<br>- more sedation/painkiller.<br>- having a general anaesthetic.</li>
    </ul>
  </div>
  <div class="copy" style="left:299px;top:516px;width:272px">
    <p>If you decide to undergo surgery awake or sedated, there is a risk you will need to have a general anaesthetic if you feel pain. This is why the starvation instructions of awake surgery and general anaesthesia are the same.</p>
  </div>

  <div class="marker" style="top:575px"></div>
  <h2 class="heading" style="top:580px">How is it done</h2>
  <div class="copy" style="left:23px;top:600px;width:272px">
    <div class="sub" style="margin-bottom:5px">If you choose awake surgery or surgery with sedation:</div>
    <ul class="list">
      <li>Numbing liquid is injected around the nerves which supply your foot.</li>
      <li>The ankle block takes 5-10 minutes to perform and requires 4-5 injections.</li>
      <li>Approximately 10-20 minutes to make your foot numb to pain.</li>
      <li>I will check the ankle block is working before we start surgery using cold spray.</li>
      <li>Sensations of touch, pressure, vibration and movement will still be felt.</li>
      <li>I will use a screen so you can’t see the surgery (unless you would like to see).</li>
      <li>Some patients bring headphones to block out the noise of the operation.</li>
    </ul>
  </div>
  <div class="copy" style="left:299px;top:600px;width:272px">
    <div class="sub" style="margin-bottom:5px">If you choose a General anaesthetic:</div>
    <ul class="list">
      <li>I will perform the ankle block after I start the general anaesthetic.</li>
      <li>You should wake up from your surgery with a comfortable and numb foot/feet</li>
      <li>If you wake in pain, we can repeat the ankle block or provide traditional painkillers.</li>
    </ul>
  </div>
  <div class="notice"><b>Whatever you choose:</b>There will be a cannula placed in your hand and heart and oxygen monitoring throughout.</div>

  <div class="hospital" style="left:214px">Riverside Gate Hospital<small>part of Meridian Healthcare UK</small></div>
  <div class="rule" style="left:14px;width:559px"></div>
  <div class="copyright">© 2018 Dr Tobias Wendell</div>
</section>

<section class="page page--two">
  <div class="clinic-name"><i></i>The Ashbury Clinic</div>

  <div class="marker" style="top:113px"></div>
  <h2 class="heading" style="top:117px">After surgery</h2>
  <div class="copy" style="left:23px;top:139px;width:270px">
    <p>You will go to the recovery area and then onto the ward when you area ready. It will be difficult to walk while the block is working so physiotherapists will help you first walk. If you need crutches they will teach you how to use them.</p>
    <p>Your foot will be numb and so you will not feel where your foot is in relation to nearby objects. As a result, it is easy to knock your foot. Please take extra care while your foot is still numb.</p>
    <p>As the block wears off, the foot may feel slightly painful, tingly or hot. At this point you should take your painkillers I have prescribed. Depending on your medical history you will have up to three painkillers. I would suggest to start with all three. You will also have an anti - sickness prescribed if one of the painkillers (typically codeine or morphine) makes you feel sick.</p>
  </div>
  <div class="copy" style="left:299px;top:139px;width:270px">
    <p>Occasionally (1-2%), pain when the block wears off will be severe. In this case contact your surgeon’s secretary. We can use stronger pain medication, but there will be charge in writing and getting the private prescription to you (please see my terms of business) via courier.</p>
  </div>

  <div class="band" style="top:325px;width:588px;height:109px">
    <div class="marker marker--light" style="top:13px"></div>
    <h2 class="heading" style="top:18px">The alternative</h2>
  </div>
  <ul class="alt-list">
    <li>If you do not have an ankle block your surgery can still proceed.</li>
    <li>Post operative pain can be managed with traditional painkillers.</li>
    <li>However, you are more likely to need an overnight stay or feel sick after the anaesthetic.</li>
  </ul>

  <div class="marker" style="top:454px"></div>
  <div class="copy" style="left:23px;top:460px;width:270px">
    <p>If you have any further questions about an ankle block I will see you the day of your surgery. Alternatively, you can request the following optional services (as mentioned in my terms of business).</p>
  </div>

  <div class="hospital" style="left:212px">Riverside Gate Hospital<small>part of Meridian Healthcare UK</small></div>
  <div class="rule" style="left:14px;width:573px"></div>
  <div class="copyright">© 2018 Dr Tobias Wendell</div>
</section>

</body>
</html>
```